Academy Values Classroom Poster

Marrowdene Community Academy has the core values of Aspiration, Positivity, Responsibility and Achievement at its heart. We have these words displayed in our entrance (in Bliss font) but would like them to permeate into the classroom spaces in a poster form. We want a clear message that shows what the values mean to students:

Aspiration - Think BIG (pantone 717)
Positivity - Smile :-) (pantone 376)
Responsibility - for yourself and others (pantone 569)
Achievement - Celebrate Success! (pantone 214)

It would be good to follow the colour scheme of the main words to create a 'brand' for these values (pantone refs noted in brackets) and we would like to see some clean designs please.

I anticipate these will be A1 posters.

I have attached our school logo although it is not essential that this is included.

Target Market(s)

Students

Industry/Entity Type

School

Font styles to use
Other font styles liked:
• Bliss or Segoe UI

Requirements
Must have
• Aspiration - Think BIG
Positivity - Smile :-)
Responsibility - for yourself and others
Achievement - Celebrate Success!
Should not have
• Nothing too busy

```html
<!DOCTYPE html>
<html lang="en">
<head>
<meta charset="utf-8">
<title>Marrowdene Community Academy – Our Values</title>
<link href="https://fonts.googleapis.com/css2?family=Jost:wght@700&display=swap" rel="stylesheet">
<style>
  :root {
    --aspiration: #f18a21;
    --positivity: #8dc63f;
    --responsibility: #00857a;
    --achievement: #d4145a;
    --ink: #3a3f4a;
    --crest: #1f3050;
    --paper: #ffffff;
  }
  html, body {
    margin: 0;
    padding: 0;
    overflow: hidden;
    background: var(--paper);
  }
  .poster {
    position: relative;
    width: 900px;
    height: 1200px;
    background: var(--paper);
    font-family: "Jost", "Segoe UI", sans-serif;
    font-weight: 700;
    text-transform: uppercase;
    overflow: hidden;
  }
  .value-word,
  .value-meaning {
    position: absolute;
    left: 0;
    width: 936px;
    text-align: center;
    line-height: 1;
    margin: 0;
    white-space: nowrap;
    font-weight: 700;
    letter-spacing: 0.5px;
  }
  .value-word.aspiration { font-size: 44px; }
  .value-word.positivity { font-size: 42px; }
  .value-word.responsibility { font-size: 40.5px; }
  .value-word.achievement { font-size: 40px; }

  .value-meaning.aspiration { font-size: 36px; }
  .value-meaning.positivity { font-size: 36px; }
  .value-meaning.responsibility { font-size: 27px; }
  .value-meaning.achievement { font-size: 30px; }

  .aspiration { color: var(--aspiration); }
  .positivity { color: var(--positivity); }
  .responsibility { color: var(--responsibility); }
  .achievement { color: var(--achievement); }

  .smile-ornament {
    position: absolute;
    left: 412px;
    top: 856px;
    width: 108px;
    height: 28px;
    border-radius: 14px;
    background: var(--ink);
  }
  .academy-mark {
    position: absolute;
    left: 0;
    width: 936px;
    top: 1072px;
    display: flex;
    justify-content: center;
    align-items: center;
    gap: 8px;
    color: var(--crest);
    font-size: 15px;
    text-transform: none;
    letter-spacing: 0.2px;
  }
  .academy-mark .mark-square {
    width: 22px;
    height: 22px;
    background: var(--crest);
  }
</style>
</head>
<body>
  <main class="poster">
    <h1 class="value-word aspiration" style="top:288px">Aspiration</h1>
    <p class="value-meaning aspiration" style="top:335px">Think Big</p>

    <h2 class="value-word positivity" style="top:406px">Positivity</h2>
    <p class="value-meaning positivity" style="top:453px">Smile :-)</p>

    <h2 class="value-word responsibility" style="top:551px">Responsibility</h2>
    <p class="value-meaning responsibility" style="top:597px">For yourself and others</p>

    <h2 class="value-word achievement" style="top:685px">Achievement</h2>
    <p class="value-meaning achievement" style="top:732px">Celebrate success!</p>

    <div class="smile-ornament" role="img" aria-label="Decorative smile ornament"></div>

    <footer class="academy-mark">
      <span class="mark-square"></span>
      <span class="academy-name">Marrowdene Community Academy</span>
    </footer>
  </main>
</body>
</html>
```